Board Presentation template

Design a simple and clean PowerPoint slide templates for a Board meeting. The slides should have predominantly white backgrounds and use the colors of our Logo (attached): Tones of grey and orange and blue.
The company name is called Harbor Crest Gauges.
It sell, calibrate, service and repair industrial and commercial scales of all types. In particular, Truck scales, floor scales, counting scales and benchtop scales.
There is no website for Harbor Crest Gauges, but we have three affiliates that have their own websites:
https://www.fernmoorweigh.com/
https://lantovalegaugeandbalance.com/
https://qtwegh.com/
Target Market(s)
Industrial and Commercial Weighing systems
Industry/Entity Type
Look and feel
Each slider illustrates characteristics of the customer's brand and the style your logo design should communicate.

```html
<!DOCTYPE html>
<html lang="en">
<head>
<meta charset="utf-8">
<title>Harbor Crest Gauges – Board Presentation Slides</title>
<link href="https://fonts.googleapis.com/css2?family=Poppins:ital,wght@0,400;0,500;0,600;0,700;1,400;1,500&display=swap" rel="stylesheet">
<style>
:root{
  --red:#d23c31;
  --blue:#1f5d96;
  --dark:#3c4853;
  --mid:#6b7580;
  --light:#a0a6ad;
  --line:#c9cdd1;
  --page:#dcdee1;
  --white:#ffffff;
}
*{margin:0;padding:0;box-sizing:border-box}
html,body{width:1200px;height:1171px;overflow:hidden;background:var(--page);font-family:"Poppins",sans-serif;color:var(--dark)}
.board{position:relative;width:1200px;height:1171px}
.slide{position:absolute;width:570px;height:320px;background:var(--white);transform:scale(0.6148);transform-origin:0 0;box-shadow:0 3px 8px rgba(0,0,0,.18);overflow:hidden}
.abs{position:absolute}
.heading{position:absolute;left:20px;top:14px;font-size:19px;font-weight:400;color:var(--dark);letter-spacing:-.2px}
.heading b{font-weight:700}
.heading::after{content:"";position:absolute;left:0;top:33px;width:45px;height:4px;border-radius:2px;background:var(--red)}
.brand{position:absolute;right:14px;top:24px;width:62px;text-align:center;font-size:6.5px;font-weight:600;line-height:1.15;color:var(--dark);letter-spacing:.3px}
.foot{position:absolute;left:20px;right:14px;top:298px;height:10px;border-bottom:1px solid var(--dark)}
.foot span{position:absolute;left:14px;top:0;font-size:3.5px;color:var(--mid)}
.foot i{position:absolute;left:0;top:-3px;width:8px;height:8px;border-radius:50%;border:1px solid var(--dark)}
.foot em{position:absolute;right:0;top:-2px;font-style:normal;font-size:6px;color:var(--dark)}
.lorem{font-size:5.6px;line-height:1.4;color:var(--light)}
.t-red{color:var(--red)} .t-blue{color:var(--blue)}
.photo{position:absolute}
/* slide positions */
.s1{left:55px;top:55px}.s2{left:425px;top:55px}.s3{left:795px;top:55px}
.s4{left:55px;top:270px}.s5{left:425px;top:270px}.s6{left:795px;top:270px}
.s7{left:55px;top:486px}.s8{left:425px;top:486px}.s9{left:795px;top:486px}
.s10{left:55px;top:701px}.s11{left:425px;top:701px}.s12{left:795px;top:701px}
.s13{left:55px;top:918px}.s14{left:425px;top:918px}.s15{left:795px;top:918px}
/* cover */
.cover-mark{left:7px;top:7px;width:8px;height:8px;background:var(--dark)}
.cover-name{left:35px;top:95px;width:140px;font-size:13px;font-weight:600;line-height:1.15;color:var(--dark)}
.cover-title{left:35px;top:150px;font-weight:700;line-height:1}
.cover-title .l1{font-size:25px;color:var(--red)}
.cover-title .l2{font-size:29px;color:var(--dark);margin-top:2px}
.cover-sub{left:35px;top:220px;font-size:13px;font-style:italic;font-weight:500;color:var(--blue)}
.cover-text{left:35px;top:240px;width:160px;font-style:italic}
.dots{left:35px;top:286px;display:flex;gap:4px}
.dots i{width:5px;height:5px;border-radius:50%;background:var(--dark)}
/* toc */
.toc-title{position:absolute;left:22px;top:14px;font-size:20px;color:var(--dark)}
.toc-title b{font-weight:600}
.toc-title::after{content:"";position:absolute;left:0;top:34px;width:45px;height:4px;border-radius:2px;background:var(--red)}
.toc-item{position:absolute;width:215px;height:14px;font-size:7.5px;font-weight:500;color:var(--dark);padding-left:8px}
.toc-item::before{content:"";position:absolute;left:0;top:5px;width:3px;height:3px;border-radius:50%;background:var(--red)}
.toc-item::after{content:"";position:absolute;left:8px;right:16px;top:11px;border-bottom:1px solid var(--line)}
.toc-item b{position:absolute;right:0;top:0;width:13px;height:13px;border-radius:50%;background:var(--dark);color:#fff;font-size:5.5px;text-align:center;line-height:13px}
/* misc */
.icon-sq{position:absolute;width:48px;height:48px;border-radius:8px;background:var(--red)}
.h-sm{font-size:11px;font-weight:600;color:var(--dark)}
.num-h{font-size:10px;font-weight:600;color:var(--dark)}
.bullets{position:absolute;left:310px;top:80px;list-style:none}
.bullets li{font-size:10px;color:var(--dark);height:31px;padding-left:8px;position:relative}
.bullets li::before{content:"";position:absolute;left:0;top:6px;width:3px;height:3px;border-radius:50%;background:var(--red)}
.flow-box{position:absolute;width:96px;height:146px;border:4px solid var(--dark);border-radius:10px;text-align:center;padding:36px 8px 0}
.flow-box h4{font-size:7.5px;font-weight:600;color:var(--red);margin-bottom:6px}
.flow-box .lorem{font-size:4.3px}
.panel{position:absolute;left:312px;top:72px;width:196px;height:198px;border-radius:14px;background:var(--dark)}
.panel-item{position:absolute;left:346px;width:150px;color:#fff}
.panel-item h5{font-size:9px;font-weight:600}
.panel-item p{font-size:5px;line-height:1.3;color:#e3e6e8}
.red-dot{position:absolute;width:40px;height:40px;border-radius:50%;background:var(--red);border:3px solid #fff;box-shadow:0 0 0 1px var(--line)}
.list-h{font-size:7px;font-weight:600;color:var(--blue)}
.list-h b{color:var(--dark)}
.num-circle{position:absolute;width:34px;height:34px;border-radius:50%;color:#fff;font-size:12px;font-weight:700;text-align:center;line-height:34px}
.tile{position:absolute;width:91px;height:88px;border-radius:4px;padding:40px 8px 0;color:#fff}
.tile h5{font-size:7px;font-weight:600;margin-bottom:3px}
.tile p{font-size:3.8px;line-height:1.35}
.tile svg{position:absolute;left:10px;top:12px}
.col-h{font-size:13px;font-weight:600;color:var(--blue);margin-bottom:4px}
.col-h b{color:var(--red)}
.quad-text{position:absolute;width:130px}
.quad-text h5{font-size:8px;font-weight:600;color:var(--dark)}
.quad-text p{font-size:4.8px;line-height:1.35;color:var(--mid)}
.step-text{position:absolute;width:80px;text-align:center;top:190px}
.step-text h5{font-size:7.5px;font-weight:600;color:var(--dark)}
.step-text p{font-size:3.8px;line-height:1.4;color:var(--light)}
.yr-t{position:absolute;width:90px;text-align:center}
.yr-t h5{font-size:6.5px;font-weight:600;color:var(--dark)}
.yr-t p{font-size:5px;line-height:1.35;color:var(--light)}
.card{position:absolute;width:84px;text-align:center;top:88px}
.card .top{height:32px}
.card .avatar{width:44px;height:44px;border-radius:50%;margin:-22px auto 0;border:3px solid #fff;background:linear-gradient(180deg,#e6e2dd,#b9b2aa)}
.card h5{font-size:8px;font-weight:600;margin-top:6px}
.card p{font-size:3.8px;line-height:1.4;color:var(--light);margin-top:3px}
.thanks{left:335px;top:65px;font-size:33px;font-weight:700;color:var(--dark)}
.contact{position:absolute;left:340px;width:210px;display:flex;gap:6px;align-items:center;font-size:6px;line-height:1.35;color:var(--dark)}
.contact span{border-left:1px solid var(--dark);padding-left:5px}
.end-name{left:40px;top:130px;width:230px;font-size:22px;font-weight:600;line-height:1.15;color:var(--dark)}
.end-sq{left:40px;top:105px;width:14px;height:14px;background:var(--red)}
</style>
</head>
<body>
<main class="board">

<!-- 1 Cover -->
<section class="slide s1">
  <div class="abs cover-mark"></div>
  <div class="abs cover-name">HARBOR CREST GAUGES</div>
  <div class="abs cover-title"><div class="l1">Business</div><div class="l2">Marketing</div></div>
  <div class="abs cover-sub">Presentation</div>
  <p class="abs cover-text lorem">Lorem ipsum dolor sit amet, consectetuer adipiscing elit, sed diam nonum</p>
  <div class="abs dots"><i></i><i></i><i></i></div>
  <div class="abs" style="left:415px;top:0;width:155px;height:140px;background:var(--red)"></div>
  <div class="abs" style="left:237px;top:200px;width:333px;height:120px;background:var(--blue)"></div>
  <div class="abs" style="left:258px;top:20px;width:292px;height:270px;background:#fff"></div>
  <div class="photo" role="img" aria-label="Photo of a blue heavy truck loaded with cargo parked on a dirt yard" style="left:276px;top:36px;width:260px;height:240px;background:linear-gradient(180deg,#d9c8b6 0%,#9fb2c4 35%,#2d5fa6 60%,#8b7a63 100%)"></div>
</section>

<!-- 2 Table of Contents -->
<section class="slide s2">
  <h2 class="toc-title">Table of <b>Contents</b></h2>
  <div class="brand">HARBOR CREST GAUGES</div>
  <div class="toc-item" style="left:52px;top:95px">Simple Text One<b>02</b></div>
  <div class="toc-item" style="left:52px;top:128px">Simple Text Two<b>04</b></div>
  <div class="toc-item" style="left:52px;top:161px">Simple Text Three<b>06</b></div>
  <div class="toc-item" style="left:52px;top:194px">Simple Text Four<b>08</b></div>
  <div class="toc-item" style="left:52px;top:227px">Simple Text Five<b>10</b></div>
  <div class="toc-item" style="left:299px;top:95px">Simple Text One<b>02</b></div>
  <div class="toc-item" style="left:299px;top:128px">Simple Text Two<b>04</b></div>
  <div class="toc-item" style="left:299px;top:161px">Simple Text Three<b>06</b></div>
  <div class="toc-item" style="left:299px;top:194px">Simple Text Four<b>08</b></div>
  <div class="toc-item" style="left:299px;top:227px">Simple Text Five<b>10</b></div>
  <div class="foot"><i></i><span>© 2024 Harbor Crest Gauges. All rights reserved.</span><em>2</em></div>
</section>

<!-- 3 Mission & Vision -->
<section class="slide s3">
  <h2 class="heading"><b>Heading</b> Goes Here</h2>
  <div class="brand">HARBOR CREST GAUGES</div>
  <p class="abs lorem" style="left:32px;top:66px;width:230px;font-size:7px;font-style:italic;color:var(--mid)">Lorem ipsum dolor sit amet, cons ectetuer adipiscing elit, sed diam nonummy nibh euismod tincidunt. Lorem ipsum dolor sit amet.</p>
  <div class="photo" role="img" aria-label="Photo of a man with arms crossed standing in front of an orange truck" style="left:32px;top:120px;width:233px;height:136px;background:linear-gradient(90deg,#5b5f63 0%,#8a8d90 35%,#c0392b 50%,#e07a26 70%,#6d7074 100%)"></div>
  <div class="icon-sq" style="left:307px;top:98px"></div>
  <div class="abs" style="left:366px;top:100px;width:160px">
    <div class="h-sm"><b>Our</b> <span class="t-red">Mission</span></div>
    <p class="lorem" style="font-size:6.5px;font-style:italic">Lorem ipsum dolor sit amet, cons ectetuer adipiscing elit, sed diam nonummy nibh euismod tincidunt.</p>
  </div>
  <div class="icon-sq" style="left:307px;top:189px"></div>
  <div class="abs" style="left:366px;top:190px;width:160px">
    <div class="h-sm"><b>Our</b> <span class="t-blue">Vision</span></div>
    <p class="lorem" style="font-size:6.5px;font-style:italic">Lorem ipsum dolor sit amet, cons ectetuer adipiscing elit, sed diam nonummy nibh euismod tincidunt.</p>
  </div>
  <div class="foot"><i></i><span>© 2024 Harbor Crest Gauges. All rights reserved.</span><em>3</em></div>
</section>

<!-- 4 Text and bullets -->
<section class="slide s4">
  <h2 class="heading"><b>Heading</b> Goes Here</h2>
  <div class="brand">HARBOR CREST GAUGES</div>
  <div class="abs" style="left:45px;top:66px;width:235px">
    <div class="num-h"><span class="t-red">01.</span> Text Added Here</div>
    <p class="lorem" style="text-align:justify">Lorem ipsum dolor sit amet, cons ectetuer adipiscing elit, sed diam nonummy nibh euismod tincidunt ut laoreet dolore magna aliquam erat volutpat. Ut wisi enim ad minim veniam, quis nostrud exerci tation ullamcorper suscipit lobortis nisl ut aliquip ex ea commodo consequat.</p>
    <p class="lorem" style="text-align:justify;margin-top:4px">Lorem ipsum dolor sit amet, consectetuer adipiscing elit, sed diam nonummy nibh euismod tincidunt ut laoreet dolore magna aliquam erat volutpat. Ut wisi enim ad minim veniam, quis nostrud exerci tation ullamcorper suscipit lobortis nisl ut aliquip ex ea commodo.</p>
    <div class="num-h" style="margin-top:8px"><span class="t-red">02.</span> Text Added Here</div>
    <p class="lorem" style="text-align:justify">Lorem ipsum dolor sit amet, cons ectetuer adipiscing elit, sed diam nonummy nibh euismod tincidunt ut laoreet dolore magna aliquam erat volutpat. Ut wisi enim ad minim veniam, quis nostrud exerci tation ullamcorper suscipit lobortis nisl ut aliquip ex ea commodo consequat.</p>
    <p class="lorem" style="margin-top:4px">Lorem ipsum dolor sit amet, consectetuer adipiscing elit, sed diam</p>
  </div>
  <ul class="bullets">
    <li>Fits Your Business Or Products</li>
    <li>Is Easy To Spell And Remember</li>
    <li>Fits Your Business Or Products</li>
    <li>Is Easy To Spell And Remember</li>
    <li>Fits Your Business Or Products</li>
    <li>Is Easy To Spell And Remember</li>
  </ul>
  <div class="foot"><i></i><span>© 2024 Harbor Crest Gauges. All rights reserved.</span><em>4</em></div>
</section>

<!-- 5 Idea / Promotion / Growth -->
<section class="slide s5">
  <h2 class="heading"><b>Heading</b> Goes Here</h2>
  <div class="brand">HARBOR CREST GAUGES</div>
  <div class="flow-box" style="left:105px;top:78px">
    <svg class="abs" style="left:38px;top:14px" width="12" height="16" viewBox="0 0 12 16"><path d="M6 1a5 5 0 0 0-3 9v2h6v-2a5 5 0 0 0-3-9z M4 14h4" fill="none" stroke="#3a6ea5" stroke-width="1.2"/></svg>
    <h4>IDEA</h4><p class="lorem">Lorem ipsum dolor sit amet, consectetuer adipiscing elit, sed diam nonummy nibh euismod tincidunt ut laoreet dolore magna aliquam erat volutpat. Ut wisi enim ad minim veniam, quis nostrud exerci tation ullamcorper suscipit lobortis nisl ut</p>
  </div>
  <div class="flow-box" style="left:235px;top:78px">
    <svg class="abs" style="left:36px;top:16px" width="16" height="12" viewBox="0 0 16 12"><rect x="1" y="1" width="14" height="10" fill="none" stroke="#3a6ea5" stroke-width="1.2"/><path d="M1 1l7 6 7-6" fill="none" stroke="#3a6ea5" stroke-width="1.2"/></svg>
    <h4>PROMOTION</h4><p class="lorem">Lorem ipsum dolor sit amet, consectetuer adipiscing elit, sed diam nonummy nibh euismod tincidunt ut laoreet dolore magna aliquam erat volutpat. Ut wisi enim ad minim veniam, quis nostrud exerci tation ullamcorper suscipit lobortis nisl ut</p>
  </div>
  <div class="flow-box" style="left:365px;top:78px">
    <svg class="abs" style="left:38px;top:14px" width="14" height="14" viewBox="0 0 14 14"><path d="M1 1v12h12 M3 10l4-4 2 2 4-5" fill="none" stroke="#3a6ea5" stroke-width="1.3"/></svg>
    <h4>GROWTH</h4><p class="lorem">Lorem ipsum dolor sit amet, consectetuer adipiscing elit, sed diam nonummy nibh euismod tincidunt ut laoreet dolore magna aliquam erat volutpat. Ut wisi enim ad minim veniam, quis nostrud exerci tation ullamcorper suscipit lobortis nisl ut</p>
  </div>
  <svg class="abs" style="left:0;top:0" width="570" height="320">
    <path d="M199 200 L237 118 M329 200 L367 118" stroke="#3c4853" stroke-width="4"/>
    <circle cx="189" cy="110" r="4" fill="#3c4853"/><circle cx="237" cy="200" r="4" fill="#3c4853"/>
    <circle cx="329" cy="110" r="4" fill="#3c4853"/><circle cx="367" cy="200" r="4" fill="#3c4853"/>
  </svg>
  <p class="abs lorem" style="left:70px;top:242px;width:430px;text-align:center;font-size:6px;color:var(--mid)">Lorem ipsum dolor sit amet, consectetuer adipiscing elit, sed diam nonummy nibh euismod tincidunt ut laoreet dolore magna aliquam erat volutpat. Ut wisi enim ad minim veniam, quis nostrud exerci tation ullamcorper suscipit lobortis nisl ut aliquip ex ea commodo consequat. Duis autem vel eum iriure dolor in hendrerit</p>
  <div class="foot"><i></i><span>© 2024 Harbor Crest Gauges. All rights reserved.</span><em>5</em></div>
</section>

<!-- 6 List and dark panel -->
<section class="slide s6">
  <h2 class="heading"><b>Heading</b> Goes Here</h2>
  <div class="brand">HARBOR CREST GAUGES</div>
  <div class="abs" style="left:65px;top:76px;width:200px">
    <div class="list-h"><b>01.</b> Aliquam Erat Volutpat</div>
    <p class="lorem" style="padding-left:14px;color:var(--mid)">Lorem ipsum dolor sit amet, consectetuer adipiscing elit, sed diam nonummy nibh euismod</p>
  </div>
  <div class="abs" style="left:63px;top:128px;width:200px">
    <div class="list-h"><b>02.</b> Consectetuer Adipiscing Elit</div>
    <p class="lorem" style="padding-left:14px;color:var(--mid)">Lorem ipsum dolor sit amet, consectetuer adipiscing elit, sed diam nonummy nibh euismod tincidunt ut laoreet.</p>
  </div>
  <div class="abs" style="left:63px;top:181px;width:200px">
    <div class="list-h"><b>03.</b> Duis Autem Vel Eum</div>
    <p class="lorem" style="padding-left:14px;color:var(--mid)">Lorem ipsum dolor sit amet, consectetuer adipiscing elit, sed diam nonummy nibh euismod tincidunt.</p>
  </div>
  <div class="abs" style="left:62px;top:231px;width:200px">
    <div class="list-h"><b>04.</b> Aliquam Erat Volutpat</div>
    <p class="lorem" style="padding-left:14px;color:var(--mid)">Lorem ipsum dolor sit amet, consectetuer adipiscing elit, sed diam nonummy nibh euismod tincidunt ut laoreet.</p>
  </div>
  <div class="panel"></div>
  <div class="red-dot" style="left:290px;top:89px"></div>
  <div class="red-dot" style="left:290px;top:148px"></div>
  <div class="red-dot" style="left:290px;top:208px"></div>
  <div class="panel-item" style="top:88px"><h5>LOREM IPSUM</h5><p>ipsum dolor sit amet, cons ectetuer adipiscing elit, sed diam nonummy nibh euismod tincidunt ut laoreet</p></div>
  <div class="panel-item" style="top:146px"><h5>LOREM IPSUM</h5><p>ipsum dolor sit amet, cons ectetuer adipiscing elit, sed diam nonummy nibh euismod tincidunt ut laoreet dolore magna aliquam erat volutpat.</p></div>
  <div class="panel-item" style="top:208px"><h5>LOREM IPSUM</h5><p>ipsum dolor sit amet, cons ectetuer adipiscing elit, sed diam nonummy nibh euismod tincidunt</p></div>
  <div class="foot"><i></i><span>© 2024 Harbor Crest Gauges. All rights reserved.</span><em>6</em></div>
</section>

<!-- 7 Bar chart -->
<section class="slide s7">
  <h2 class="heading"><b>Heading</b> Goes Here</h2>
  <div class="brand">HARBOR CREST GAUGES</div>
  <svg class="abs" style="left:40px;top:85px" width="240" height="190" viewBox="0 0 240 190" font-family="Poppins, sans-serif" font-size="4.5" fill="#6b7580">
    <g stroke="#e1e4e7" stroke-width=".6">
      <line x1="12" y1="10" x2="235" y2="10"/><line x1="12" y1="30" x2="235" y2="30"/><line x1="12" y1="50" x2="235" y2="50"/><line x1="12" y1="70" x2="235" y2="70"/><line x1="12" y1="90" x2="235" y2="90"/><line x1="12" y1="110" x2="235" y2="110"/><line x1="12" y1="130" x2="235" y2="130"/>
    </g>
    <text x="6" y="12">6</text><text x="6" y="32">5</text><text x="6" y="52">4</text><text x="6" y="72">3</text><text x="6" y="92">2</text><text x="6" y="112">1</text><text x="6" y="132">0</text>
    <rect x="28" y="22" width="11" height="108" fill="#d23c31"/><rect x="41" y="38" width="11" height="92" fill="#3c4853"/><rect x="54" y="64" width="11" height="66" fill="#1f5d96"/>
    <rect x="88" y="22" width="11" height="108" fill="#d23c31"/><rect x="101" y="2" width="11" height="128" fill="#3c4853"/><rect x="114" y="46" width="11" height="84" fill="#1f5d96"/>
    <rect x="146" y="18" width="11" height="112" fill="#d23c31"/><rect x="159" y="64" width="11" height="66" fill="#3c4853"/><rect x="172" y="46" width="11" height="84" fill="#1f5d96"/>
    <text x="36" y="143">Category 1</text><text x="95" y="143">Category 1</text><text x="152" y="143">Category 1</text>
    <rect x="64" y="149" width="3" height="3" fill="#d23c31"/><text x="69" y="152" font-size="3.5">Series 1</text>
    <rect x="87" y="149" width="3" height="3" fill="#3c4853"/><text x="92" y="152" font-size="3.5">Series 1</text>
    <rect x="110" y="149" width="3" height="3" fill="#1f5d96"/><text x="115" y="152" font-size="3.5">Series 1</text>
  </svg>
  <div class="num-circle" style="left:301px;top:84px;background:var(--red)">1</div>
  <div class="num-circle" style="left:301px;top:150px;background:var(--dark)">2</div>
  <div class="num-circle" style="left:301px;top:216px;background:var(--blue)">3</div>
  <div class="abs" style="left:345px;top:78px;width:180px"><div class="h-sm t-red" style="font-size:9.5px">Lorem ipsum dolor.</div><p class="lorem" style="font-size:6.5px;color:var(--mid)">Lorem ipsumectetuer adipiscing elit, sed diam nonummy nibh euismod tincidunt sed diam nonummy nibhunt</p></div>
  <div class="abs" style="left:345px;top:144px;width:180px"><div class="h-sm" style="font-size:9.5px">Lorem ipsum dolor.</div><p class="lorem" style="font-size:6.5px;color:var(--mid)">Lorem ipsumectetuer adipiscing elit, sed diam nonummy nibh euismod tincidunt sed diam nonummy nibhunt</p></div>
  <div class="abs" style="left:345px;top:210px;width:180px"><div class="h-sm t-blue" style="font-size:9.5px">Lorem ipsum dolor.</div><p class="lorem" style="font-size:6.5px;color:var(--mid)">Lorem ipsumectetuer adipiscing elit, sed diam nonummy nibh euismod tincidunt sed diam nonummy nibhunt</p></div>
  <div class="foot"><i></i><span>© 2024 Harbor Crest Gauges. All rights reserved.</span><em>7</em></div>
</section>

<!-- 8 Photo and text -->
<section class="slide s8">
  <h2 class="heading"><b>Heading</b> Goes Here</h2>
  <div class="brand">HARBOR CREST GAUGES</div>
  <div class="photo" role="img" aria-label="Photo of a white semi truck with trailer driving on a road under a blue sky" style="left:48px;top:70px;width:192px;height:188px;background:linear-gradient(180deg,#2f74c4 0%,#a9cdeb 40%,#eef2f5 60%,#7fa35a 85%,#6e7a5a 100%)"></div>
  <div class="abs" style="left:270px;top:72px;width:242px">
    <div class="num-h t-blue">01. Text Added Here</div>
    <p class="lorem" style="text-align:justify;color:var(--mid)">Lorem ipsum dolor sit amet, cons ectetuer adipiscing elit, sed diam nonummy nibh euismod tincidunt ut laoreet dolore magna aliquam erat volutpat. Ut wisi enim ad minim veniam, quis nostrud exerci tation ullamcorper suscipit lobortis nisl ut aliquip ex ea commodo consequat.</p>
    <div class="num-h t-blue" style="margin-top:9px">02. Text Added Here</div>
    <p class="lorem" style="text-align:justify;color:var(--mid)">Lorem ipsum dolor sit amet, cons ectetuer adipiscing elit, sed diam nonummy nibh euismod tincidunt ut laoreet dolore magna aliquam erat volutpat. Ut wisi enim ad minim veniam, quis nostrud exerci tation ullamcorper suscipit lobortis nisl ut aliquip ex ea commodo consequat.</p>
    <div class="num-h t-blue" style="margin-top:9px">03. Text Added Here</div>
    <p class="lorem" style="text-align:justify;color:var(--mid)">Lorem ipsum dolor sit amet, cons ectetuer adipiscing elit, sed diam nonummy nibh euismod tincidunt ut laoreet dolore magna aliquam erat volutpat. Ut wisi enim ad minim veniam, quis nostrud exerci tation ullamcorper suscipit lobortis nisl ut aliquip ex ea commodo consequat.</p>
  </div>
  <div class="foot"><i></i><span>© 2024 Harbor Crest Gauges. All rights reserved.</span><em>8</em></div>
</section>

<!-- 9 Problem / Solution tiles -->
<section class="slide s9">
  <h2 class="heading"><b>Heading</b> Goes Here</h2>
  <div class="brand">HARBOR CREST GAUGES</div>
  <div class="abs" style="left:38px;top:108px;width:140px"><div class="list-h" style="font-size:8px">01. Project Problem</div><p class="lorem" style="font-size:4.8px">Lorem ipsum dolor sit amet, cons ectetuer adipiscing elit, sed diam nonummy nibh euismod tincidunt Lorem ipsum dolor sit amet</p></div>
  <div class="abs" style="left:191px;top:108px;width:140px"><div class="list-h" style="font-size:8px">02. Project Solution</div><p class="lorem" style="font-size:4.8px">Lorem ipsum dolor sit amet, cons ectetuer adipiscing elit, sed diam nonummy nibh euismod tincidunt Lorem ipsum dolor sit amet</p></div>
  <div class="abs" style="left:38px;top:186px;width:140px"><div class="list-h" style="font-size:8px">03. Project Problem</div><p class="lorem" style="font-size:4.8px">Lorem ipsum dolor sit amet, cons ectetuer adipiscing elit, sed diam nonummy nibh euismod tincidunt Lorem ipsum dolor sit amet</p></div>
  <div class="abs" style="left:191px;top:186px;width:140px"><div class="list-h" style="font-size:8px">04. Project Solution</div><p class="lorem" style="font-size:4.8px">Lorem ipsum dolor sit amet, cons ectetuer adipiscing elit, sed diam nonummy nibh euismod tincidunt Lorem ipsum dolor sit amet</p></div>
  <div class="tile" style="left:341px;top:82px;background:var(--dark)"><svg width="12" height="12" viewBox="0 0 12 12"><circle cx="6" cy="6" r="4" fill="none" stroke="#fff"/></svg><h5>PROBLEM</h5><p>Lorem ipsum dolor sit amet, cons ectetuer adipiscing elit, sed diam nonummy.</p></div>
  <div class="tile" style="left:437px;top:82px;background:var(--red)"><svg width="12" height="12" viewBox="0 0 12 12"><path d="M6 1a3.5 3.5 0 0 0-2 6.4V9h4V7.4A3.5 3.5 0 0 0 6 1z" fill="none" stroke="#fff"/></svg><h5>SOLUTION</h5><p>Lorem ipsum dolor sit amet, cons ectetuer adipiscing elit, sed diam nonummy.</p></div>
  <div class="tile" style="left:341px;top:173px;background:var(--red)"><svg width="12" height="12" viewBox="0 0 12 12"><path d="M1 11h10 M3 11V7 M6 11V4 M9 11V2" stroke="#fff"/></svg><h5>MARKET</h5><p>Lorem ipsum dolor sit amet, cons ectetuer adipiscing elit, sed diam nonummy.</p></div>
  <div class="tile" style="left:437px;top:173px;background:var(--dark)"><svg width="12" height="12" viewBox="0 0 12 12"><circle cx="6" cy="6" r="5" fill="none" stroke="#fff"/><circle cx="6" cy="6" r="2" fill="none" stroke="#fff"/></svg><h5>MISSION</h5><p>Lorem ipsum dolor sit amet, cons ectetuer adipiscing elit, sed diam nonummy.</p></div>
  <div class="foot"><i></i><span>© 2024 Harbor Crest Gauges. All rights reserved.</span><em>9</em></div>
</section>

<!-- 10 Two columns -->
<section class="slide s10">
  <h2 class="heading"><b>Heading</b> Goes Here</h2>
  <div class="brand">HARBOR CREST GAUGES</div>
  <div class="abs" style="left:48px;top:72px;width:222px">
    <div class="col-h"><b>01.</b> Text Added Here</div>
    <p class="lorem" style="text-align:justify;color:var(--mid)">Lorem ipsum dolor sit amet, cons ectetuer adipiscing elit, sed diam nonummy nibh euismod tincidunt ut laoreet dolore magna aliquam erat volutpat. Ut wisi enim ad minim veniam, quis nostrud exerci tation ullamcorper suscipit lobortis nisl ut aliquip ex ea commodo consequat. Lorem ipsum dolor sit amet, consectetuer adipiscing elit, sed diam nonummy nibh euismod tincidunt ut laoreet dolore magna aliquam erat volutpat. Utostrud exerci tation ullamcorper suscipit lobortis nisl ut aliquip ex ea commodo consequat.</p>
    <p class="lorem" style="text-align:justify;color:var(--mid);margin-top:6px">Lorem ipsum dolor sit amet, cons ectetuer adipiscing elit, sed diam nonummy nibh euismod tincidunt ut laoreet dolore magna aliquam erat volutpat. Ut wisi enim ad minim veniam, quis nostrud exerci tation ullamcorper suscipit lobortis nisl ut aliquip ex ea commodo consequat.</p>
    <p class="lorem" style="text-align:justify;color:var(--mid);margin-top:6px">Lorem ipsum dolor sit amet, consectetuer adipiscing elit, sed diam nonummy nibh euismod tincidunt ut laoreet dolore magna aliquam erat volutpat. Ut wisi enim ad minim veniam, cons ectetuer adipiscing elit, volutpat. veniam, quis nostrud exerci tation ullamcorper suscipit lobortis nisl ut aliquip.</p>
  </div>
  <div class="abs" style="left:295px;top:72px;width:222px">
    <div class="col-h"><b>02.</b> Text Added Here</div>
    <p class="lorem" style="text-align:justify;color:var(--mid)">Lorem ipsum dolor sit amet, cons ectetuer adipiscing elit, sed diam nonummy nibh euismod tincidunt ut laoreet dolore magna aliquam erat volutpat. Ut wisi enim ad minim veniam, quis nostrud exerci tation ullamcorper suscipit lobortis nisl ut aliquip ex ea commodo consequat. Lorem ipsum dolor sit amet, consectetuer adipiscing elit, sed diam nonummy nibh euismod tincidunt ut laoreet dolore magna aliquam erat volutpat. Utostrud exerci tation ullamcorper suscipit lobortis nisl ut aliquip ex ea commodo consequat.</p>
    <p class="lorem" style="text-align:justify;color:var(--mid);margin-top:6px">Lorem ipsum dolor sit amet, cons ectetuer adipiscing elit, sed diam nonummy nibh euismod tincidunt ut laoreet dolore magna aliquam erat volutpat. Ut wisi enim ad minim veniam, quis nostrud exerci tation ullamcorper suscipit lobortis nisl ut aliquip ex ea commodo consequat.</p>
    <p class="lorem" style="text-align:justify;color:var(--mid);margin-top:6px">Lorem ipsum dolor sit amet, consectetuer adipiscing elit, sed diam nonummy nibh euismod tincidunt ut laoreet dolore magna aliquam erat volutpat. Ut wisi enim ad minim veniam, quis nostrud exerci tation ullamcorper suscipit lobortis nisl ut aliquip.</p>
  </div>
  <div class="foot"><i></i><span>© 2024 Harbor Crest Gauges. All rights reserved.</span><em>10</em></div>
</section>

<!-- 11 Ring diagram -->
<section class="slide s11">
  <h2 class="heading"><b>Heading</b> Goes Here</h2>
  <div class="brand">HARBOR CREST GAUGES</div>
  <svg class="abs" style="left:206px;top:80px" width="160" height="160" viewBox="-80 -80 160 160" font-family="Poppins, sans-serif">
    <g stroke="#fff" stroke-width="2.5">
      <path d="M-78 0 A78 78 0 0 1 0 -78 L0 -38 A38 38 0 0 0 -38 0 Z" fill="#d23c31"/>
      <path d="M0 -78 A78 78 0 0 1 78 0 L38 0 A38 38 0 0 0 0 -38 Z" fill="#1f5d96"/>
      <path d="M78 0 A78 78 0 0 1 0 78 L0 38 A38 38 0 0 0 38 0 Z" fill="#d23c31"/>
      <path d="M0 78 A78 78 0 0 1 -78 0 L-38 0 A38 38 0 0 0 0 38 Z" fill="#1f5d96"/>
    </g>
    <circle cx="-38" cy="-38" r="8" fill="none" stroke="#fff" stroke-width="1.5"/>
    <circle cx="38" cy="-38" r="8" fill="none" stroke="#fff" stroke-width="1.5"/>
    <circle cx="38" cy="38" r="8" fill="none" stroke="#fff" stroke-width="1.5"/>
    <circle cx="-38" cy="38" r="8" fill="none" stroke="#fff" stroke-width="1.5"/>
    <text x="0" y="-3" text-anchor="middle" font-size="12" font-weight="600" fill="#3c4853">Text</text>
    <text x="0" y="12" text-anchor="middle" font-size="12" font-weight="600" fill="#3c4853">Added</text>
  </svg>
  <div class="quad-text" style="left:60px;top:80px;text-align:right"><h5>Text Here</h5><p>Lorem ipsum dolor sit amet, cons ectetuer adipiscing elit, sed diammy nibh euismod tincidunt ut laoreet dolore</p></div>
  <div class="quad-text" style="left:381px;top:80px"><h5>Text Here</h5><p>Lorem ipsum dolor sit amet, consectetuer adipiscing elit, sed diammy nibh euismod tincidunt ut laoreet dolore</p></div>
  <div class="quad-text" style="left:60px;top:195px;text-align:right"><h5>Text Here</h5><p>Lorem ipsum dolor sit amet, consectetuer adipiscing elit, sed diammy nibh euismod tincidunt ut laoreet dolore</p></div>
  <div class="quad-text" style="left:381px;top:195px"><h5>Text Here</h5><p>Lorem ipsum dolor sit amet, consectetuer adipiscing elit, sed diammy nibh euismod tincidunt ut laoreet dolore</p></div>
  <div class="foot"><i></i><span>© 2024 Harbor Crest Gauges. All rights reserved.</span><em>11</em></div>
</section>

<!-- 12 Steps -->
<section class="slide s12">
  <h2 class="heading"><b>Heading</b> Goes Here</h2>
  <div class="brand">HARBOR CREST GAUGES</div>
  <svg class="abs" style="left:0;top:0" width="570" height="200" font-family="Poppins, sans-serif">
    <rect x="45" y="148" width="125" height="9" fill="#3c4853"/>
    <rect x="170" y="148" width="100" height="9" fill="#d23c31"/>
    <rect x="270" y="148" width="100" height="9" fill="#3c4853"/>
    <rect x="370" y="148" width="150" height="9" fill="#d23c31"/>
    <path d="M518 144 L528 152.5 L518 161 Z" fill="#d23c31"/>
    <g fill="#fff" stroke-width="9">
      <circle cx="137" cy="123" r="26" stroke="#3c4853"/>
      <circle cx="237" cy="123" r="26" stroke="#d23c31"/>
      <circle cx="337" cy="123" r="26" stroke="#3c4853"/>
      <circle cx="437" cy="123" r="26" stroke="#d23c31"/>
    </g>
    <circle cx="137" cy="123" r="10" fill="none" stroke="#1f5d96" stroke-width="1.5"/><path d="M137 117v6h4" stroke="#1f5d96" stroke-width="1.5" fill="none"/>
    <circle cx="237" cy="123" r="9" fill="#1f5d96"/><text x="237" y="127" text-anchor="middle" font-size="10" fill="#fff">$</text>
    <ellipse cx="337" cy="117" rx="9" ry="3" fill="#1f5d96"/><rect x="328" y="119" width="18" height="4" fill="#1f5d96"/><rect x="328" y="125" width="18" height="4" fill="#1f5d96"/>
    <circle cx="434" cy="120" r="7" fill="none" stroke="#1f5d96" stroke-width="2"/><path d="M429 125l-6 6" stroke="#1f5d96" stroke-width="2.5"/>
    <text x="155" y="155" font-size="5" font-weight="600" fill="#fff">Step 01</text>
    <text x="255" y="155" font-size="5" font-weight="600" fill="#fff">Step 02</text>
    <text x="355" y="155" font-size="5" font-weight="600" fill="#fff">Step 03</text>
    <text x="472" y="155" font-size="5" font-weight="600" fill="#fff">Step 04</text>
    <g stroke="#3c4853" stroke-width="1.5"><line x1="137" y1="166" x2="137" y2="178"/><line x1="237" y1="166" x2="237" y2="178"/><line x1="337" y1="166" x2="337" y2="178"/><line x1="437" y1="166" x2="437" y2="178"/></g>
  </svg>
  <div class="step-text" style="left:97px"><h5>Lorem Ipsum</h5><p>Lorem ipsum dolor sit amet, consectetuer adipiscing elit, sed diam nonummy nibh euismod tincidunt ut laoreet dolore magna aliquam erat volutpat. Ut wisi</p></div>
  <div class="step-text" style="left:197px"><h5>Lorem Ipsum</h5><p>Lorem ipsum dolor sit amet, consectetuer adipiscing elit, sed diam nonummy nibh euismod tincidunt ut laoreet dolore magna aliquam erat volutpat. Ut wisi</p></div>
  <div class="step-text" style="left:297px"><h5>Lorem Ipsum</h5><p>Lorem ipsum dolor sit amet, consectetuer adipiscing elit, sed diam nonummy nibh euismod tincidunt ut laoreet dolore magna aliquam erat volutpat. Ut wisi</p></div>
  <div class="step-text" style="left:397px"><h5>Lorem Ipsum</h5><p>Lorem ipsum dolor sit amet, consectetuer adipiscing elit, sed diam nonummy nibh euismod tincidunt ut laoreet dolore magna aliquam erat volutpat. Ut wisi</p></div>
  <div class="foot"><i></i><span>© 2024 Harbor Crest Gauges. All rights reserved.</span><em>12</em></div>
</section>

<!-- 13 Years timeline -->
<section class="slide s13">
  <h2 class="heading"><b>Heading</b> Goes Here</h2>
  <div class="brand">HARBOR CREST GAUGES</div>
  <svg class="abs" style="left:0;top:0" width="570" height="260" font-family="Poppins, sans-serif">
    <g stroke="#d23c31" stroke-width="1.5">
      <line x1="101" y1="132" x2="101" y2="150"/><line x1="285" y1="132" x2="285" y2="150"/><line x1="470" y1="132" x2="470" y2="150"/>
      <line x1="194" y1="190" x2="194" y2="206"/><line x1="378" y1="190" x2="378" y2="206"/>
    </g>
    <g fill="#d23c31"><circle cx="101" cy="132" r="3"/><circle cx="285" cy="132" r="3"/><circle cx="470" cy="132" r="3"/><circle cx="194" cy="206" r="3"/><circle cx="378" cy="206" r="3"/></g>
    <path d="M62 180 L74 162 L148 162 L136 180 Z" fill="#3c4853"/>
    <path d="M138 162 L242 162 L230 180 L150 180 Z" fill="#1f5d96"/>
    <path d="M244 162 L320 162 L332 180 L232 180 Z" fill="#3c4853"/>
    <path d="M322 162 L428 162 L416 180 L334 180 Z" fill="#1f5d96"/>
    <path d="M430 162 L506 162 L518 180 L418 180 Z" fill="#3c4853"/>
    <g font-size="6" font-weight="600" fill="#fff" text-anchor="middle">
      <text x="105" y="174">1990</text><text x="190" y="174">2001</text><text x="282" y="174">2007</text><text x="375" y="174">2012</text><text x="468" y="174">2020</text>
    </g>
  </svg>
  <div class="yr-t" style="left:56px;top:88px"><h5>YOUR TITLE</h5><p>Refers to a good or service being offered</p></div>
  <div class="yr-t" style="left:240px;top:88px"><h5>YOUR TITLE</h5><p>Refers to a good or service being offered</p></div>
  <div class="yr-t" style="left:425px;top:88px"><h5>YOUR TITLE</h5><p>Refers to a good or service being offered</p></div>
  <div class="yr-t" style="left:149px;top:216px"><h5>YOUR TITLE</h5><p>Refers to a good or service being offered</p></div>
  <div class="yr-t" style="left:333px;top:216px"><h5>YOUR TITLE</h5><p>Refers to a good or service being offered</p></div>
  <div class="foot"><i></i><span>© 2024 Harbor Crest Gauges. All rights reserved.</span><em>13</em></div>
</section>

<!-- 14 Team -->
<section class="slide s14">
  <h2 class="heading"><b>Heading</b> Goes Here</h2>
  <div class="brand">HARBOR CREST GAUGES</div>
  <div class="card" style="left:52px"><div class="top" style="background:var(--dark)"></div><div class="avatar" role="img" aria-label="Portrait photo of team member"></div><h5 class="t-blue">OWEN HALE</h5><p>ipsum dolor sit amet, cons ectetuer adipiscing elit, sed diam nonummy nibh euismod tincidunt</p><p>ut laoreet dolore magna aliquam erat volutpat. Ut wisi enim ad minim veniam, quis nostrud</p></div>
  <div class="card" style="left:177px"><div class="top" style="background:var(--red)"></div><div class="avatar" role="img" aria-label="Portrait photo of team member"></div><h5>CLARA VOSS</h5><p>ipsum dolor sit amet, cons ectetuer adipiscing elit, sed diam nonummy nibh euismod tincidunt ut laoreet dolore magna</p><p>aliquam erat volutpat. Ut wisi enim ad minim veniam, quis nostrud</p></div>
  <div class="card" style="left:305px"><div class="top" style="background:var(--dark)"></div><div class="avatar" role="img" aria-label="Portrait photo of team member"></div><h5 class="t-blue">OWEN HALE</h5><p>ipsum dolor sit amet, cons ectetuer adipiscing elit, sed diam nonummy nibh euismod tincidunt ut laoreet dolore magna aliquam erat volutpat</p><p>Ut wisi enim ad minim veniam, quis nostrud</p></div>
  <div class="card" style="left:434px"><div class="top" style="background:var(--red)"></div><div class="avatar" role="img" aria-label="Portrait photo of team member"></div><h5>CLARA VOSS</h5><p>ipsum dolor sit amet, cons ectetuer adipiscing elit, sed diam nonummy nibh euismod tincidunt ut laoreet dolore magna</p><p>aliquam erat volutpat. Ut wisi enim ad minim veniam, quis nostrud</p></div>
  <div class="foot"><i></i><span>© 2024 Harbor Crest Gauges. All rights reserved.</span><em>14</em></div>
</section>

<!-- 15 Thank you -->
<section class="slide s15">
  <div class="abs end-sq"></div>
  <div class="abs end-name">HARBOR CREST<br>GAUGES</div>
  <div class="abs thanks">Thank You</div>
  <div class="contact" style="top:142px">
    <svg width="11" height="11" viewBox="0 0 12 12"><path d="M2 1l3 0 1 3-1.5 1a6 6 0 0 0 2.5 2.5L8 6l3 1v3c-5 1-10-4-9-9z" fill="#3c4853"/></svg>
    <span>+1 555 0142 2290<br>+1 555 0142 2290</span>
  </div>
  <div class="contact" style="top:180px">
    <svg width="11" height="11" viewBox="0 0 12 12"><path d="M1 1l10 4-4 1.5L5.5 11z" fill="#3c4853"/></svg>
    <span>www.harborcrestgauges.example<br>hello@harborcrestgauges.example</span>
  </div>
  <div class="contact" style="top:210px">
    <svg width="11" height="11" viewBox="0 0 12 12"><path d="M6 1L0.5 6H2v5h3V8h2v3h3V6h1.5z" fill="#3c4853"/></svg>
    <span>58 Quay Road, town/city,<br>state/country, post/zip 012345.</span>
  </div>
</section>

</main>
</body>
</html>
```